K-VOR Landing Page

We want to re-design our current home page on our website (www.plexamora.com) to simplify it and reduce it down to the (3) main products / services we offer. There are too many options of where they can go and it seems to be confusing for them. Additionally, we sell a higher end software product and we want the site to appear very professional for when CFO's considering our software can be confident in its quality and the long established company that we are. Our products and services are all about optimizing manufacturing production for sheet metal stampers (primarily automotive and appliance). I am including a rough power point layout of what we are thinking along with flyers for our three main products. We want to maintain the look and feel of the sample marketing materials as much as possible but does not have to match exactly. We will be producing the video ourselves to add where the power point shows a video being. Please review our website for any additional information.

```html
<!DOCTYPE html>
<html lang="en">
<head>
<meta charset="utf-8">
<title>K-VOR Solutions</title>
<link href="https://fonts.googleapis.com/css2?family=Oswald:wght@400;500;600&family=Red+Hat+Display:wght@400;500;700;800&display=swap" rel="stylesheet">
<style>
:root{
  --yellow:#f9be15;
  --yellow-soft:#fff3cf;
  --navy:#1d5a73;
  --navy-deep:#143f55;
  --ink:#222;
  --text:#444;
  --grey-bg:#f3f3f3;
  --white:#fff;
  --charcoal:#3a3a3a;
}
*{margin:0;padding:0;box-sizing:border-box}
html,body{width:1200px;height:3169px;overflow:hidden}
body{font-family:"Red Hat Display",sans-serif;color:var(--text);background:var(--white);position:relative}
a{color:inherit;text-decoration:none}
.btn{position:absolute;display:flex;align-items:center;justify-content:center;background:var(--yellow);color:var(--ink);font-weight:800;font-size:13px;border-radius:22px;text-transform:uppercase}
.brand{display:flex;align-items:center;gap:10px;font-weight:800;color:var(--charcoal);letter-spacing:1px}
.brand .mark{width:30px;height:30px;background:var(--yellow)}

/* header */
.site-header{position:absolute;left:0;top:0;width:1200px;height:79px;background:var(--white)}
.site-header .brand{position:absolute;left:141px;top:20px;font-size:32px}
.main-nav{position:absolute;left:393px;top:31px;display:flex;gap:22px;font-family:"Oswald",sans-serif;font-size:12.5px;color:var(--ink);text-transform:uppercase}
.site-header .btn{left:985px;top:24px;width:79px;height:32px;font-family:"Oswald",sans-serif;font-weight:500;font-size:12.5px}

/* hero */
.hero{position:absolute;left:0;top:79px;width:1200px;height:496px;background:linear-gradient(90deg,#2f6f8e 0%,#3b7d9a 45%,#5a9ab5 70%,#4b86a3 100%)}
.hero-art{position:absolute;left:560px;top:0;width:640px;height:496px;background:radial-gradient(circle at 60% 45%,#f0d7b8 0%,#8fb6c9 28%,rgba(60,120,150,0) 62%)}
.hero h1{position:absolute;left:141px;top:118px;font-family:"Oswald",sans-serif;font-weight:600;font-size:57px;line-height:64px;color:var(--white);text-transform:uppercase}
.hero p{position:absolute;left:143px;top:252px;font-weight:700;font-size:15.5px;line-height:24px;color:var(--white)}
.hero .btn{left:141px;top:317px;width:174px;height:42px}

/* about */
.about-back{position:absolute;left:180px;top:668px;width:394px;height:436px;background:var(--yellow-soft);border-radius:56px 0 56px 0}
.about-photo{position:absolute;left:141px;top:680px;width:410px;height:409px;border-radius:52px 0 52px 0;background:linear-gradient(135deg,#5a6f80,#2e4456 60%,#7d8c98)}
.about-text{position:absolute;left:617px;top:718px;width:450px}
.eyebrow{color:var(--yellow);font-weight:800;font-size:22px;line-height:26px}
.about-text h2{font-weight:800;font-size:38px;color:var(--ink);line-height:44px;margin-bottom:10px}
.about-text p{font-size:15.5px;line-height:28px;color:var(--text)}
.about-cta{left:616px;top:990px;width:174px;height:42px}

/* services */
.services-bg{position:absolute;left:0;top:1195px;width:1200px;height:455px;background:var(--grey-bg)}
.services-title{position:absolute;left:0;top:1270px;width:1200px;text-align:center;font-weight:800;font-size:33px;line-height:46px;color:var(--ink)}
.service-card{position:absolute;top:1397px;width:284px;height:410px;background:var(--white);border-radius:14px;box-shadow:0 4px 14px rgba(0,0,0,.06);text-align:center;padding:0 18px;border-bottom:4px solid}
.service-card .icon{width:110px;height:110px;border-radius:50%;margin:26px auto 22px;display:flex;align-items:center;justify-content:center}
.service-card h3{font-weight:700;font-size:15.5px;line-height:22px;color:var(--ink);text-transform:uppercase;margin-bottom:6px}
.service-card p{font-size:11.8px;line-height:21.6px;color:var(--text)}
.outline-btn{position:absolute;left:50%;transform:translateX(-50%);top:346px;width:137px;height:36px;border:1.5px solid var(--ink);border-radius:20px;display:flex;align-items:center;justify-content:center;font-weight:800;font-size:12px;color:var(--ink)}

/* features */
.features-title{position:absolute;left:0;top:1882px;width:1200px;text-align:center;font-weight:800;font-size:36px;color:var(--ink)}
.feature{position:absolute;width:212px;height:185px;background:var(--white);border-radius:14px;box-shadow:0 3px 14px rgba(0,0,0,.07);text-align:center;padding:0 16px}
.feature .ficon{width:76px;height:76px;margin:14px auto 12px;border-radius:50%;background:var(--yellow-soft);display:flex;align-items:center;justify-content:center}
.feature p{font-weight:700;font-size:13px;line-height:18.5px;color:var(--ink)}
.feature-brand{font-size:34px;justify-content:center;margin-top:44px}
.feature .btn{left:20px;top:106px;width:173px;height:42px}

/* guarantee */
.guarantee{position:absolute;left:0;top:2465px;width:1200px;height:314px;background:linear-gradient(90deg,#1d5f80,#236a8c 50%,#1b5675)}
.guarantee h2{position:absolute;left:181px;top:68px;font-weight:800;font-size:36px;color:var(--white)}
.guarantee p{position:absolute;left:182px;top:117px;font-size:21px;line-height:31px;color:var(--white)}
.guarantee p b{font-weight:800}
.guarantee .btn{left:181px;top:203px;width:174px;height:42px}
.badge{position:absolute;left:785px;top:50px}

/* footer */
.site-footer{position:absolute;left:0;top:2779px;width:1200px;height:344px}
.site-footer h4{position:absolute;top:80px;font-weight:800;font-size:16px;color:var(--ink)}
.quick-links{position:absolute;left:142px;top:111px;list-style:none;font-size:13px;line-height:24.5px;color:var(--text)}
.contact-item{position:absolute;left:374px;display:flex;gap:8px;font-size:12.8px;line-height:19px;color:var(--text)}
.social{position:absolute;left:671px;top:106px;list-style:none}
.social li{display:flex;align-items:center;gap:10px;font-size:13px;height:37px;color:var(--text)}
.social .dot{width:25px;height:25px;border-radius:50%;background:var(--yellow)}
.footer-brand{position:absolute;left:843px;top:70px;font-size:44px}
.footer-blurb{position:absolute;left:837px;top:150px;width:225px;font-size:11.5px;line-height:21.5px;color:var(--text)}
.copyright{position:absolute;left:0;top:3123px;width:1200px;height:46px;background:var(--yellow);display:flex;align-items:center;justify-content:center;font-size:13px;color:var(--ink)}
</style>
</head>
<body>

<header class="site-header">
  <div class="brand"><span class="mark"></span>K-VOR</div>
  <nav class="main-nav">
    <a>About</a><a>How We Help</a><a>K-VOR Software</a><a>Transfer Simulation Service</a><a>Business Case</a><a>Resources</a>
  </nav>
  <a class="btn">Contact</a>
</header>

<section class="hero">
  <div class="hero-art" role="img" aria-label="Hand touching a glowing network of gear and technology icons over a blurred city skyline"></div>
  <h1>We Are K-VOR Solutions<br>Provides Software</h1>
  <p>And Service For Transfer Press Simulation &amp; Optimization<br>On New And Existing Tooling.</p>
  <a class="btn">Contact Us Today</a>
</section>

<section class="about">
  <div class="about-back"></div>
  <div class="about-photo" role="img" aria-label="Team of colleagues gathered around a laptop in an office"></div>
  <div class="about-text">
    <div class="eyebrow">ABOUT</div>
    <h2>K-VOR SOLUTIONS</h2>
    <p>At our core, we are a software company committed to providing cuttingedge simulation and optimization solutions. However, we understand that our customers have diverse needs and requirements which may not fit with buying software at this time. That’s why we offer&nbsp; flexible options for you to experience the power of K-VOR.</p>
  </div>
  <a class="btn about-cta">Contact Us Today</a>
</section>

<section class="services">
  <div class="services-bg"></div>
  <h2 class="services-title">INCREASE PRODUCTION AND ELIMINATE HEADACHES<br>WITH K-VOR PRODUCTS AND SERVICES</h2>

  <article class="service-card" style="left:141px;border-color:var(--yellow)">
    <div class="icon" style="background:var(--yellow)">
      <svg width="60" height="60" viewBox="0 0 60 60" fill="none" stroke="#222" stroke-width="2.5"><circle cx="30" cy="36" r="14"/><circle cx="30" cy="36" r="7"/><path d="M30 20V6M22 10l8-8 8 8M16 24V12M11 16l5-5 5 5M44 24V12M39 16l5-5 5 5"/><path d="M24 40l5-5 3 3 5-6"/></svg>
    </div>
    <h3>New Tool Simulation<br>and Optimization</h3>
    <p>Are you starting a new transfer tooling program soon? Trust the experts at K-VOR to make it the best one you’ve ever had! Know your production rates before you build and confidently launch your tooling at the HIGHEST possible production rates</p>
    <a class="outline-btn">REQUEST A QUOTE</a>
  </article>

  <article class="service-card" style="left:460px;border-color:var(--navy)">
    <div class="icon" style="background:var(--navy)">
      <svg width="60" height="60" viewBox="0 0 60 60" fill="none" stroke="#fff" stroke-width="2.5"><circle cx="32" cy="20" r="11"/><circle cx="32" cy="20" r="4"/><path d="M32 5v4M32 31v4M17 20h4M43 20h4"/><path d="M6 42h10l10 4h10a3 3 0 010 6H24M36 48l14-8a3 3 0 013 5L38 56H6"/></svg>
    </div>
    <h3>Existing Tool Optimization<br>(With or Without CAD)</h3>
    <p>Are you at capacity in your transfer press, running your equipment harder than you’d like, or simply know you can be doing better? Our existing tool optimization service is a great way increase your production efficiency (OEE) and free up press capacity.</p>
    <a class="outline-btn">REQUEST A QUOTE</a>
  </article>

  <article class="service-card" style="left:780px;border-color:var(--charcoal)">
    <div class="icon" style="background:var(--charcoal)">
      <svg width="60" height="60" viewBox="0 0 60 60" fill="none" stroke="#fff" stroke-width="2.5"><rect x="6" y="14" width="40" height="28" rx="2"/><path d="M20 50h14M27 42v8"/><path d="M12 36V28M18 36V24M24 36V30"/><circle cx="44" cy="16" r="8"/><circle cx="44" cy="16" r="3"/></svg>
    </div>
    <h3>K-VOR Software<br>Products</h3>
    <p>Without question, our most successful customers are the ones who use the software themselves. K-VOR Users typically see as much as 40% increase in their production rates! Hard to believe? Try it and see for yourself!</p>
    <a class="outline-btn">REQUEST A QUOTE</a>
  </article>
</section>

<section class="features">
  <h2 class="features-title">KEY FEATURES AND BENEFITS</h2>

  <div class="feature" style="left:141px;top:1973px">
    <div class="ficon"><svg width="48" height="48" viewBox="0 0 48 48" fill="none" stroke="#1d5a73" stroke-width="2"><rect x="6" y="8" width="26" height="30"/><path d="M12 32V24M18 32V20M24 32V26"/><path d="M10 18l10-8 8 4 12-10" stroke="#f9be15"/><circle cx="34" cy="32" r="7"/><path d="M39 37l6 6"/></svg></div>
    <p>Increase press capacity (OEE) and reduce downtime</p>
  </div>
  <div class="feature" style="left:378px;top:1973px">
    <div class="ficon"><svg width="48" height="48" viewBox="0 0 48 48" fill="none" stroke="#1d5a73" stroke-width="2"><path d="M6 44V20l8-8 8 8v24M14 12V4"/><circle cx="30" cy="28" r="7" stroke="#f9be15"/><circle cx="30" cy="28" r="2.5" stroke="#f9be15"/><path d="M26 44V38h8v6M38 20l6-6 6 6"/></svg></div>
    <p>Reduce wear and tear on equipment with optimized curves.</p>
  </div>
  <div class="feature" style="left:614px;top:1973px">
    <div class="ficon"><svg width="48" height="48" viewBox="0 0 48 48" fill="none" stroke="#1d5a73" stroke-width="2"><circle cx="18" cy="22" r="12"/><circle cx="18" cy="22" r="5"/><path d="M34 8c6 6 6 18 0 30h-6c-4-12-4-22 6-30z" stroke="#f9be15"/><path d="M28 38l-4 6M34 38l4 6"/></svg></div>
    <p>Make new tooling launches headache free!</p>
  </div>
  <div class="feature" style="left:851px;top:1973px">
    <div class="ficon"><svg width="48" height="48" viewBox="0 0 48 48" fill="none" stroke="#1d5a73" stroke-width="2"><circle cx="18" cy="16" r="7"/><circle cx="18" cy="16" r="2.5"/><rect x="32" y="4" width="8" height="8"/><rect x="32" y="20" width="8" height="8"/><path d="M25 16h7M36 12v8"/><path d="M4 40h8l8-6h14l-6 6 12-4" stroke="#f9be15"/></svg></div>
    <p>Easily move projects from press to press with optimized settings</p>
  </div>

  <div class="feature" style="left:141px;top:2195px">
    <div class="ficon"><svg width="48" height="48" viewBox="0 0 48 48" fill="none" stroke="#1d5a73" stroke-width="2"><circle cx="22" cy="22" r="15"/><path d="M22 12v10l7 5"/><path d="M32 34l10 10M36 30l8 8" stroke="#f9be15"/></svg></div>
    <p>Increase time for preventative maintenance</p>
  </div>
  <div class="feature" style="left:378px;top:2195px">
    <div class="ficon"><svg width="48" height="48" viewBox="0 0 48 48" fill="none" stroke="#1d5a73" stroke-width="2"><rect x="4" y="20" width="28" height="20"/><path d="M4 26h28"/><circle cx="32" cy="16" r="10" stroke="#f9be15"/><circle cx="32" cy="16" r="4" stroke="#f9be15"/></svg></div>
    <p>Optimize both new and existing tooling</p>
  </div>
  <div class="feature" style="left:614px;top:2195px">
    <div class="ficon"><svg width="48" height="48" viewBox="0 0 48 48" fill="none" stroke="#1d5a73" stroke-width="2"><rect x="8" y="6" width="24" height="34"/><path d="M14 14h12M14 20h12M14 26h8"/><circle cx="34" cy="34" r="8" stroke="#f9be15"/><circle cx="34" cy="34" r="3" stroke="#f9be15"/></svg></div>
    <p>Optimize projects with or without CAD</p>
  </div>
  <div class="feature" style="left:851px;top:2195px">
    <div class="brand feature-brand"><span class="mark"></span>K-VOR</div>
    <a class="btn">Contact Us Today</a>
  </div>
</section>

<section class="guarantee">
  <h2>OUR GUARANTEE</h2>
  <p>You’ll make your money back in your&nbsp; <b>first (5) projects</b> or<br>we’ll refund the entire purchase price!</p>
  <a class="btn">Contact Us Today</a>
  <svg class="badge" width="210" height="210" viewBox="0 0 210 210" role="img" aria-label="Money back guarantee seal">
    <circle cx="105" cy="105" r="104" fill="#f9be15"/>
    <circle cx="105" cy="105" r="82" fill="#2a2a2a"/>
    <circle cx="105" cy="105" r="52" fill="#f9be15"/>
  </svg>
</section>

<footer class="site-footer">
  <h4 style="left:141px">QUICK LINKS</h4>
  <ul class="quick-links">
    <li>Home</li><li>About</li><li>How We Help</li><li>K-Vor Software</li><li>Transfer Simulation Service</li><li>Business Case</li><li>Resources</li><li>Contact</li>
  </ul>

  <h4 style="left:374px">CONTACT DETAILS</h4>
  <div class="contact-item" style="top:104px">
    <svg width="12" height="16" viewBox="0 0 12 16"><path d="M6 0a6 6 0 016 6c0 4-6 10-6 10S0 10 0 6a6 6 0 016-6z" fill="#333"/><circle cx="6" cy="6" r="2.2" fill="#fff"/></svg>
    <span>PO Box 412 · 88 Corvel Industrial<br>Dr. Lanford, MI 49000-0412</span>
  </div>
  <div class="contact-item" style="top:157px">
    <svg width="13" height="13" viewBox="0 0 24 24"><path d="M6.6 10.8a15 15 0 006.6 6.6l2.2-2.2a1 1 0 011-.25 11.4 11.4 0 003.6.6 1 1 0 011 1V20a1 1 0 01-1 1A17 17 0 013 4a1 1 0 011-1h3.5a1 1 0 011 1c0 1.25.2 2.45.6 3.6a1 1 0 01-.25 1z" fill="#333"/></svg>
    <span>Phone<br>555-204-7781</span>
  </div>
  <div class="contact-item" style="top:209px">
    <svg width="13" height="13" viewBox="0 0 24 24"><rect x="1" y="4" width="22" height="16" fill="none" stroke="#333" stroke-width="2"/><path d="M1 4l11 9 11-9" fill="none" stroke="#333" stroke-width="2"/></svg>
    <span>Email<br>info@plexamora.com</span>
  </div>

  <h4 style="left:671px">FOLLOW US</h4>
  <ul class="social">
    <li><span class="dot"></span>Friendloop</li>
    <li><span class="dot"></span>Chirpline</li>
    <li><span class="dot"></span>Vidnest</li>
    <li><span class="dot"></span>Snapgrid</li>
  </ul>

  <div class="brand footer-brand"><span class="mark" style="width:40px;height:40px"></span>K-VOR</div>
  <p class="footer-blurb">At our core, we are a software company committed to providing cuttingedge simulation and optimization solutions....</p>
</footer>

<div class="copyright">© 2024 K-VOR SOLUTIONS. All Rights Reserved</div>

</body>
</html>
```